Modern Business Card Design for Independent Urban Music Label

We need a card design for an independent urban music label called Copper Field Studio based in London. We develop and promote urban British music artists. We attend lots of high profile events with high profile industry people and want a card that comes across both on-brand and sophisticated, professional, trustworthy. I have attached our logo - please use the black and orange version in the upper left HOWEVER we are open to seeing other colors than the orange used though we want the shape of the logo to remain the same.

Info to please include:
Name
Position
Phone
Email
Website

Additional Info:
Twitter: @CopperFieldStudioUK
Insta: @CopperFieldStudio

Target Market(s)

Industry professionals and others artists

Industry/Entity Type

Business

Contact Information for Business Card

Info to please include:
Name
Position
Phone
Email
Website

Additional Info:
Twitter: @CopperFieldStudioUK
Insta: @CopperFieldStudio

Requirements
Must have
• Logo, company name
• Info to please include:
• Name
• Position
• Phone
• Email
• Website
Nice to have
• Twitter: @CopperFieldStudioUK
• Insta: @CopperFieldStudio
• If it can be done so that it doesn't look cluttered

```html
<!DOCTYPE html>
<html lang="en">
<head>
<meta charset="utf-8">
<title>Copper Field Studio – Business Card</title>
<link rel="stylesheet" href="https://fonts.googleapis.com/css2?family=Open+Sans:wght@400;600&display=swap">
<style>
  :root {
    --ink: #141414;
    --paper: #ffffff;
    --copper: #ee8a44;
    --backdrop: #e9e6e3;
  }
  * { box-sizing: border-box; margin: 0; padding: 0; }
  html, body {
    width: 1200px;
    height: 1000px;
    overflow: hidden;
    background: var(--backdrop);
    font-family: "Open Sans", Arial, sans-serif;
  }
  .canvas {
    position: relative;
    width: 1200px;
    height: 1000px;
    display: flex;
    justify-content: center;
    align-items: center;
    gap: 70px;
  }
  .card {
    position: relative;
    width: 360px;
    height: 580px;
    box-shadow: 0 10px 30px rgba(0,0,0,.18);
  }
  .card--front { background: var(--ink); }
  .card--back { background: var(--paper); }

  .brand {
    position: absolute;
    left: 0;
    right: 0;
    display: flex;
    justify-content: center;
    align-items: center;
    gap: 10px;
    font-weight: 600;
    letter-spacing: .08em;
    text-transform: uppercase;
  }
  .card--front .brand { top: 230px; color: var(--paper); font-size: 20px; }
  .card--back .brand { top: 150px; color: var(--copper); font-size: 17px; }
  .brand__dot {
    width: 14px;
    height: 14px;
    border-radius: 50%;
    background: currentColor;
  }

  .details {
    position: absolute;
    top: 272px;
    left: 0;
    width: 328px;
    list-style: none;
    display: flex;
    flex-direction: column;
    gap: 6px;
  }
  .details__row {
    height: 26px;
    display: flex;
    align-items: center;
    gap: 10px;
    padding-left: 10px;
    font-size: 15px;
    color: var(--paper);
  }
  .details__row--identity { background: var(--ink); padding-left: 22px; }
  .details__row--contact { background: var(--copper); }
  .details__icon {
    width: 14px;
    height: 14px;
    flex: none;
    fill: none;
    stroke: var(--paper);
    stroke-width: 1.6;
  }
  .details__marker {
    width: 10px;
    height: 10px;
    margin: 0 2px;
    flex: none;
    border-radius: 50%;
    background: var(--paper);
  }
</style>
</head>
<body>
<main class="canvas">
  <section class="card card--front" aria-label="Card front">
    <div class="brand"><span class="brand__dot"></span>Copper Field Studio</div>
  </section>

  <section class="card card--back" aria-label="Card back">
    <div class="brand"><span class="brand__dot"></span>Copper Field Studio</div>
    <ul class="details">
      <li class="details__row details__row--identity">Name</li>
      <li class="details__row details__row--identity">Promotions Manager</li>
      <li class="details__row details__row--contact">
        <svg class="details__icon" viewBox="0 0 14 14" aria-hidden="true"><rect x="4" y="1" width="6" height="12" rx="1"/><line x1="6" y1="11" x2="8" y2="11"/></svg>
        02071234567
      </li>
      <li class="details__row details__row--contact">
        <svg class="details__icon" viewBox="0 0 14 14" aria-hidden="true"><rect x="1" y="3" width="12" height="8"/><polyline points="1,3 7,8 13,3"/></svg>
        hello@copperfieldstudio.com
      </li>
      <li class="details__row details__row--contact">
        <svg class="details__icon" viewBox="0 0 14 14" aria-hidden="true"><circle cx="7" cy="7" r="6"/><ellipse cx="7" cy="7" rx="2.5" ry="6"/><line x1="1" y1="7" x2="13" y2="7"/></svg>
        www.copperfieldstudio.com
      </li>
      <li class="details__row details__row--contact">
        <span class="details__marker" aria-hidden="true"></span>
        @CopperFieldStudioUK
      </li>
      <li class="details__row details__row--contact">
        <span class="details__marker" aria-hidden="true"></span>
        @CopperFieldStudio
      </li>
    </ul>
  </section>
</main>
</body>
</html>
```